Movie Poster/DVD jacket for Short Documentary

I am a documentary filmmaker who just completed a project titled "Sister Marigold". Here is the logline (short description of the movie): "An Oklahoma family is ripped apart after their 15-year-old son brutally murders his older sister in 1974. Controversy swirls around the case after his parents decide to hire a prominent defense attorney to keep him out of jail." I have several good photos of the family involved. I am in the process of submitting the film to several festivals and I want a professional looking movie poster that can be sent with film submissions. The look needs to dramatic and serious.
Updates

Project Deadline Extended Reason: We just had several more submission enter today and need a few more days to evaluate. Thank you for you patience. Added Thursday, November 19, 2015

Target Market(s)

Film festivals, television

Industry/Entity Type

Movie

Colors
f04a50

Requirements
Must have
• the color red and have a similar appearance to the sample movie posters.
• Also, tagline: turning a blind eye into broken hearts
• Directors name: a film by Rob Haskett
Nice to have
• rough
Should not have
• Not a gruesome look.

```html
<!DOCTYPE html>
<html lang="en">
<head>
<meta charset="utf-8">
<title>Sister Marigold — Poster</title>
<link rel="stylesheet" href="https://fonts.googleapis.com/css2?family=PT+Sans&family=Rubik+Dirt&family=Silkscreen&display=swap">
<style>
  :root {
    --page: #ffffff;
    --frame: #2e2123;
    --poster-red: #e12a36;
    --collar-red: #c9242c;
    --collar-shadow: rgba(60, 0, 5, 0.45);
    --lining: #dc7363;
    --lining-shade: #c26455;
    --ink: #2a1416;
    --pendant-light: #b3161f;
    --pendant-dark: #2a0a0c;
  }
  html, body {
    margin: 0;
    width: 1200px;
    height: 1200px;
    overflow: hidden;
    background: var(--page);
  }
  .poster {
    position: absolute;
    left: 166px;
    top: 6px;
    width: 856px;
    height: 1186px;
    box-sizing: border-box;
    border: 29px solid var(--frame);
    background: var(--poster-red);
    overflow: hidden;
    box-shadow: 0 0 3px rgba(0,0,0,0.25);
  }
  .artwork {
    position: absolute;
    inset: 0;
  }
  .credit {
    position: absolute;
    left: 62px;
    top: 275px;
    width: 300px;
    text-align: center;
    font-family: "PT Sans", sans-serif;
    color: var(--ink);
    line-height: 1.05;
  }
  .credit .credit-lead { font-size: 29px; letter-spacing: 0.5px; }
  .credit .credit-by { font-size: 36px; }
  .credit .credit-name { font-size: 50px; margin-top: 2px; }
  .title {
    position: absolute;
    left: 14px;
    top: 520px;
    width: 390px;
    margin: 0;
    font-family: "Rubik Dirt", system-ui, sans-serif;
    font-weight: 400;
    color: var(--ink);
    text-transform: uppercase;
    font-size: 62px;
    line-height: 1.25;
    text-align: center;
  }
  .title .initial { font-size: 1.3em; }
  .tagline {
    position: absolute;
    left: 10px;
    top: 1048px;
    width: 790px;
    height: 40px;
  }
  .tagline text {
    font-family: "Silkscreen", monospace;
    font-size: 29px;
    fill: var(--ink);
  }
</style>
</head>
<body>
  <div class="poster">
    <svg class="artwork" width="798" height="1128" viewBox="0 0 798 1128" xmlns="http://www.w3.org/2000/svg">
      <defs>
        <filter id="collar-drop" x="-20%" y="-20%" width="140%" height="140%">
          <feDropShadow dx="0" dy="8" stdDeviation="10" flood-color="#3c0005" flood-opacity="0.5"/>
        </filter>
        <radialGradient id="pendant-tone" cx="40%" cy="45%" r="65%">
          <stop offset="0" stop-color="var(--pendant-light)"/>
          <stop offset="1" stop-color="var(--pendant-dark)"/>
        </radialGradient>
      </defs>
      <g class="collar" filter="url(#collar-drop)">
        <path class="collar-band" fill="var(--collar-red)"
              d="M101 0 L53 141 L267 125 L560 635 Q585 665 612 640 L798 382 L798 0 Z"/>
      </g>
      <path class="collar-lining" fill="var(--lining)"
            d="M253 0 L798 0 L798 255 L587 593 Z"/>
      <path class="collar-lining-shade" fill="var(--lining-shade)"
            d="M253 0 L320 0 L600 572 L587 593 Z"/>
      <rect class="pendant" role="img" aria-label="Heart-shaped pendant with a rifle hanging from a chain at the collar"
            x="305" y="745" width="493" height="295" rx="40" fill="url(#pendant-tone)"/>
    </svg>

    <div class="credit">
      <div class="credit-lead">A FILM</div>
      <div class="credit-by">BY</div>
      <div class="credit-name">Rob Haskett</div>
    </div>

    <h1 class="title">
      <span class="initial">S</span>ister<br>
      <span class="initial">M</span>arigold
    </h1>

    <svg class="tagline" viewBox="0 0 790 40" xmlns="http://www.w3.org/2000/svg">
      <text x="0" y="32" textLength="785" lengthAdjust="spacingAndGlyphs">TURNING A BLIND EYE INTO BROKEN HEARTS</text>
    </svg>
  </div>
</body>
</html>
```